Thank you for shopping with us business card

We would like a thank you card for our rebranded business. We used to be "Kestrel Knacks" but are now "Kestrel Trinkets. Old thank you card and new logo will be attached for reference. New thank you card does not have to be same design as old thank you card, but please use new logo.
Mopsa URL is now kestreltrinkets.mopsa.com
Pictaloo is @Kestrel_Trinkets
Email is kestreltrinkets@mopsamail.com
Thank you!

Contact Information for Business Card

Mopsa site, email, Pictaloo

```html
<!DOCTYPE html>
<html lang="en">
<head>
<meta charset="utf-8">
<title>Kestrel Trinkets – Thank You Card</title>
<link rel="stylesheet" href="https://fonts.googleapis.com/css2?family=Didact+Gothic&family=Mulish:wght@700&family=Tinos:ital@1&display=swap">
<style>
  :root {
    --page: #ffffff;
    --ink-dark: #44455b;
    --sky: #52c8e8;
    --white: #ffffff;
  }
  * { margin: 0; padding: 0; box-sizing: border-box; }
  html, body {
    width: 1200px; height: 1200px; overflow: hidden;
    background: var(--page);
  }
  .canvas { position: relative; width: 1200px; height: 1200px; }

  .card {
    position: absolute; left: 258px; width: 692px; height: 446px;
    overflow: hidden;
  }
  .card--front { top: 97px; background: var(--ink-dark); }
  .card--back { top: 664px; background: var(--sky); }

  /* Front brand lockup */
  .brand-mark {
    position: absolute; left: 112px; top: 183px;
    width: 78px; height: 78px; border-radius: 50%;
    background: var(--sky);
  }
  .brand-name {
    position: absolute; left: 211px; top: 164px;
    font-family: "Mulish", sans-serif; font-weight: 700;
    color: var(--white); font-size: 56px; line-height: 56px;
    letter-spacing: 0.5px; text-transform: uppercase;
  }

  /* Back */
  .back-wave { position: absolute; inset: 0; width: 692px; height: 446px; }
  .thanks-title {
    position: absolute; left: 17px; top: 36px;
    font-family: "Didact Gothic", sans-serif;
    color: var(--white); font-size: 43px; line-height: 52px;
    letter-spacing: 1px; text-transform: uppercase;
  }
  .thanks-message {
    position: absolute; right: 28px; top: 188px;
    font-family: "Tinos", serif; font-style: italic;
    color: var(--white); font-size: 27px; line-height: 34px;
    text-align: right;
  }
  .contact-list {
    position: absolute; left: 35px; top: 324px;
    list-style: none;
  }
  .contact-item {
    display: flex; align-items: center; gap: 18px;
    height: 24px; margin-bottom: 16.5px;
    font-family: "Mulish", sans-serif; font-weight: 700;
    color: var(--white); font-size: 19px;
  }
  .contact-icon { width: 24px; height: 24px; background: var(--white); flex: none; }
  .contact-icon--round { border-radius: 50%; }

  .footer-mark {
    position: absolute; left: 438px; top: 384px;
    width: 36px; height: 36px; border-radius: 50%;
    background: var(--white);
  }
  .footer-name {
    position: absolute; left: 484px; top: 374px;
    font-family: "Mulish", sans-serif; font-weight: 700;
    color: var(--white); font-size: 26px; line-height: 28px;
    text-transform: uppercase;
  }
</style>
</head>
<body>
<main class="canvas">
  <section class="card card--front" aria-label="Card front">
    <span class="brand-mark"></span>
    <p class="brand-name">Kestrel<br>Trinkets</p>
  </section>

  <section class="card card--back" aria-label="Card back">
    <svg class="back-wave" viewBox="0 0 1108 714" preserveAspectRatio="none" aria-hidden="true">
      <path d="M0,0 H690 C690,180 650,285 555,268 C400,242 100,215 0,393 Z" fill="var(--ink-dark)"/>
    </svg>
    <h1 class="thanks-title">Thank you for<br>your purchase</h1>
    <p class="thanks-message">Your purchase made my day and I<br>hope this package brightens yours.<br>Please come back and leave a review</p>
    <ul class="contact-list">
      <li class="contact-item"><span class="contact-icon"></span>kestreltrinkets.mopsa.com</li>
      <li class="contact-item"><span class="contact-icon contact-icon--round"></span>@Kestrel_Trinkets</li>
      <li class="contact-item"><span class="contact-icon"></span>kestreltrinkets@mopsamail.com</li>
    </ul>
    <span class="footer-mark"></span>
    <p class="footer-name">Kestrel<br>Trinkets</p>
  </section>
</main>
</body>
</html>
```